New Business Card Design Project

We want a modern business card that catches the attention of other remodeling companies as well as homeowners. We would like it to be informative but still simple.

Target Market(s)

Residential and other Business's

Contact Information for Business Card

TidyKraft
Phone number is 5152947718
Address is
4817 SW 3rd Lane
Cedar Falls, Iowa 50613
email is tidykraftia@mailorbit.net

Requirements
Must have
• Our tagline
• Reliable | Skilled | Fairly Priced

```html
<!DOCTYPE html>
<html lang="en">
<head>
<meta charset="utf-8">
<title>TidyKraft Business Card</title>
<link rel="stylesheet" href="https://fonts.googleapis.com/css2?family=Arimo:wght@400&family=Oswald:wght@500;600&display=swap">
<style>
  :root {
    --backdrop: #c9cacc;
    --card: #ffffff;
    --brand-blue: #1f5bbf;
    --ink: #3f3f3f;
    --water-light: #e3f2fc;
    --water-mid: #8fcaf0;
    --water-deep: #2f93db;
  }
  html, body {
    margin: 0;
    width: 1200px;
    height: 1034px;
    overflow: hidden;
    background: var(--backdrop);
  }
  .business-card {
    position: absolute;
    left: 75px;
    top: 217px;
    width: 1050px;
    height: 600px;
    background: var(--card);
    overflow: hidden;
    box-shadow: 0 6px 18px rgba(0,0,0,0.18);
  }
  .water-wave {
    position: absolute;
    inset: 0;
    width: 100%;
    height: 100%;
  }
  .brand {
    position: absolute;
    top: 58px;
    left: 0;
    width: 100%;
    text-align: center;
  }
  .brand-name {
    margin: 0;
    font-family: "Oswald", sans-serif;
    font-weight: 600;
    font-size: 96px;
    line-height: 1;
    letter-spacing: 2px;
    color: var(--brand-blue);
  }
  .tagline {
    margin: 10px 0 0;
    font-family: "Oswald", sans-serif;
    font-weight: 500;
    font-size: 30px;
    letter-spacing: 1px;
    color: var(--brand-blue);
  }
  .tagline .divider {
    margin: 0 8px;
  }
  .contact {
    position: absolute;
    left: 68px;
    top: 368px;
    margin: 0;
    font-family: "Arimo", sans-serif;
    font-style: normal;
    font-size: 36px;
    line-height: 47px;
    color: var(--ink);
  }
  .contact span { display: block; }
</style>
</head>
<body>
  <div class="business-card">
    <svg class="water-wave" viewBox="0 0 1050 600" role="img" aria-label="Flowing blue water wave with bubbles">
      <defs>
        <linearGradient id="waveFill" x1="0" y1="0" x2="1" y2="1">
          <stop offset="0" stop-color="#e3f2fc"/>
          <stop offset="0.45" stop-color="#8fcaf0"/>
          <stop offset="1" stop-color="#2f93db"/>
        </linearGradient>
        <linearGradient id="waveSoft" x1="0" y1="0" x2="1" y2="0">
          <stop offset="0" stop-color="#eef7fd"/>
          <stop offset="1" stop-color="#bfe0f6"/>
        </linearGradient>
      </defs>
      <path d="M0 330 C 300 420, 700 380, 1050 150 L1050 600 L0 600 Z" fill="url(#waveSoft)"/>
      <path d="M0 480 C 350 500, 760 430, 1050 270 L1050 600 L0 600 Z" fill="url(#waveFill)"/>
      <path d="M0 540 C 380 545, 780 480, 1050 360 L1050 600 L0 600 Z" fill="#2f93db" opacity="0.55"/>
    </svg>

    <header class="brand">
      <h1 class="brand-name">TidyKraft</h1>
      <p class="tagline">RELIABLE<span class="divider">|</span>SKILLED<span class="divider">|</span>FAIRLY PRICED</p>
    </header>

    <address class="contact">
      <span>4817 SW 3rd Lane</span>
      <span>Cedar Falls, Iowa 50613</span>
      <span>515.294.7718</span>
      <span>tidykraftia@mailorbit.net</span>
    </address>
  </div>
</body>
</html>
```